Stationery Design Project

We need a stationery design for a new business consulting business based in New Zealand.
We have the logo and business cards designed and we're looking for letterhead, compliments slip and PowerPoint presentation format that aligns with our business cards.
Industry/Entity Type
Business
Requirements
Must have
- same colors and format as business cards

```html
<!DOCTYPE html>
<html lang="en">
<head>
<meta charset="utf-8">
<title>Kerra Advisory – Stationery</title>
<link href="https://fonts.googleapis.com/css2?family=Arimo:ital,wght@0,400;0,700;1,400&display=swap" rel="stylesheet">
<style>
  :root {
    --board: #e3e3e3;
    --paper: #ffffff;
    --card: #d9d9d9;
    --green: #8cc63f;
    --bar-grey: #8f8f8f;
    --text-grey: #7a7a7a;
    --faint: #ececec;
    --dark: #555555;
  }
  * { margin: 0; padding: 0; box-sizing: border-box; }
  html, body { width: 1200px; height: 2618px; overflow: hidden; }
  body {
    position: relative;
    background: var(--board);
    font-family: "Arimo", Arial, sans-serif;
    color: var(--dark);
  }
  .piece { position: absolute; overflow: hidden; }
  .accent-bar { position: absolute; background: var(--green); }
  .side-bar { position: absolute; background: var(--bar-grey); }
  .label {
    position: absolute;
    font-style: italic;
    font-size: 30px;
    color: #222;
    letter-spacing: 1px;
  }
  .wordmark {
    position: absolute;
    display: flex;
    align-items: center;
    gap: 10px;
    font-weight: 700;
    color: var(--text-grey);
    white-space: nowrap;
    letter-spacing: -0.5px;
  }
  .wordmark .mark-square { background: var(--green); flex: none; }
  .ghost-word {
    position: absolute;
    font-weight: 700;
    color: var(--faint);
    letter-spacing: -4px;
    white-space: nowrap;
  }
  .glow {
    background: radial-gradient(circle at 25% 25%, #ffffff 0%, #eeeeee 25%, var(--card) 60%);
  }

  /* letterhead */
  .letterhead { left: 277px; top: 26px; width: 635px; height: 895px; background: var(--paper); }
  .contact-name { color: var(--green); font-weight: 700; font-size: 13px; }
  .contact-role { font-size: 9px; color: var(--dark); font-weight: 700; }
  .contact-lines { font-size: 10.5px; font-weight: 700; color: var(--text-grey); line-height: 13px; }
  .contact-lines .icon-line { display: flex; align-items: center; gap: 4px; }
  .dot { width: 7px; height: 7px; border-radius: 50%; background: var(--green); flex: none; }

  /* compliment slip */
  .slip-panel {
    position: absolute; left: 83px; top: 938px; width: 1019px; height: 655px;
    background: linear-gradient(90deg, #e6e6e6, #f3f3f3 30%, #f3f3f3 70%, #e6e6e6);
  }
  .slip-front { left: 277px; top: 951px; width: 635px; height: 299px; }
  .slip-back { left: 277px; top: 1272px; width: 635px; height: 299px;
    background: radial-gradient(circle at 27% 50%, #ffffff 0%, #eeeeee 20%, var(--card) 50%); }
  .slip-text { position: absolute; left: 318px; top: 80px; width: 290px; font-size: 8.5px; color: #9a9a9a; line-height: 11.5px; }
  .slip-text h3 { color: var(--green); font-size: 10px; font-weight: 700; border-bottom: 1px solid var(--green); display: inline-block; margin-bottom: 6px; }

  /* slides */
  .slide-title { left: 72px; top: 1606px; width: 652px; height: 489px; }
  .slide-content { left: 476px; top: 2110px; width: 656px; height: 491px; }
  .bullets { position: absolute; list-style: none; }
  .bullets li { display: flex; align-items: center; gap: 6px; white-space: nowrap; }
  .bullets li::before { content: ""; width: 6px; height: 6px; border-radius: 50%; background: currentColor; flex: none; }
  .bullets li span.rule { border-bottom: 1px dotted currentColor; width: 130px; margin-left: -4px; height: 10px; }
</style>
</head>
<body>

  <!-- Letterhead -->
  <div class="label" style="left:59px; top:505px;">letterhead</div>
  <section class="piece letterhead">
    <div class="accent-bar" style="left:316px; top:0; width:319px; height:26px;"></div>
    <div class="side-bar" style="left:0; top:559px; width:22px; height:336px;"></div>
    <div class="ghost-word" style="left:60px; top:26px; font-size:120px;">kerra</div>
    <div class="wordmark" style="left:125px; top:45px; font-size:44px;">
      <span class="mark-square" style="width:22px; height:22px;"></span>Kerra Advisory
    </div>
    <div style="position:absolute; left:240px; top:808px;">
      <div class="contact-name">CONSULTANT NAME</div>
      <div class="contact-role">Kerra Consultant</div>
    </div>
    <div class="contact-lines" style="position:absolute; left:395px; top:808px;">
      <div>PO Box 41820</div>
      <div>Wellington 6011 New Zealand</div>
      <div class="icon-line"><span class="dot"></span>+ 64 21 555 0142</div>
      <div class="icon-line"><span class="dot"></span>info@kerraadvisory.com</div>
      <div class="icon-line"><span class="dot"></span>www.kerraadvisory.com</div>
    </div>
  </section>

  <!-- Compliment slip -->
  <div class="slip-panel"></div>
  <div class="label" style="left:929px; top:1242px;">compliment slip</div>
  <section class="piece slip-front glow">
    <div class="accent-bar" style="left:312px; top:0; width:323px; height:24px;"></div>
    <div class="side-bar" style="left:0; top:173px; width:22px; height:126px;"></div>
    <div class="ghost-word" style="left:50px; top:0; font-size:110px; color:#e6e6e6;">kerra</div>
    <div class="wordmark" style="left:110px; top:72px; font-size:44px;">
      <span class="mark-square" style="width:22px; height:22px;"></span>Kerra Advisory
    </div>
    <div style="position:absolute; left:50px; top:180px;">
      <div class="contact-name">CONSULTANT NAME</div>
      <div class="contact-role">Kerra Consultant</div>
    </div>
    <div class="contact-lines" style="position:absolute; left:57px; top:210px;">
      <div>PO Box 41820</div>
      <div>Wellington 6011 New Zealand</div>
      <div class="icon-line"><span class="dot"></span>+ 64 21 555 0142</div>
      <div class="icon-line"><span class="dot"></span>info@kerraadvisory.com</div>
      <div class="icon-line"><span class="dot"></span>www.kerraadvisory.com</div>
    </div>
  </section>
  <section class="piece slip-back">
    <div class="wordmark" style="left:34px; top:132px; font-size:30px; gap:8px; color:var(--green);">
      <span class="mark-square" style="width:16px; height:16px;"></span>Kerra Advisory
    </div>
    <div class="slip-text">
      <h3>KERRA ADVISORY</h3>
      <p>PO Box 41820 Wellington 6011 New Zealand</p>
      <p>Phone +64 21 555 0142 info@kerraadvisory.com</p>
      <p>Strategy, planning and growth advice for business</p>
      <p>Thank you for your time and interest</p>
      <p>With compliments from the advisory team</p>
      <p>We look forward to working together</p>
    </div>
  </section>

  <!-- Presentation slides -->
  <section class="piece slide-title glow">
    <div class="accent-bar" style="left:332px; top:0; width:320px; height:31px;"></div>
    <div class="side-bar" style="left:0; top:259px; width:31px; height:230px;"></div>
    <div class="ghost-word" style="left:55px; top:35px; font-size:110px; color:#e4e4e4;">kerra</div>
    <div class="wordmark" style="left:113px; top:88px; font-size:44px;">
      <span class="mark-square" style="width:22px; height:22px;"></span>Kerra Advisory
    </div>
    <h1 style="position:absolute; left:155px; top:312px; font-size:36px; font-weight:700; color:var(--text-grey); letter-spacing:-0.5px;">Title Of Presentation</h1>
    <ul class="bullets" style="left:185px; top:358px; font-size:13px; line-height:18px; color:var(--green); font-weight:700;">
      <li>Enter Text Here<span class="rule"></span></li>
      <li>Enter Text Here<span class="rule"></span></li>
      <li>Enter Text Here<span class="rule"></span></li>
    </ul>
  </section>

  <div class="label" style="left:148px; top:2190px;">presentaion slide</div>
  <section class="piece slide-content glow">
    <div class="accent-bar" style="left:336px; top:0; width:320px; height:30px;"></div>
    <div class="side-bar" style="left:0; top:257px; width:37px; height:234px;"></div>
    <div class="ghost-word" style="left:55px; top:40px; font-size:80px; color:#e4e4e4;">kerra</div>
    <div class="wordmark" style="left:90px; top:75px; font-size:32px;">
      <span class="mark-square" style="width:16px; height:16px;"></span>Kerra Advisory
    </div>
    <h2 style="position:absolute; left:65px; top:228px; font-size:22px; font-weight:700; color:var(--green);">Enter Title</h2>
    <ul class="bullets" style="left:80px; top:258px; font-size:12px; line-height:17px; color:#8a8a8a;">
      <li>Enter Text Here<span class="rule"></span></li>
      <li>Enter Text Here<span class="rule"></span></li>
      <li>Enter Text Here<span class="rule"></span></li>
      <li>Enter Text Here<span class="rule"></span></li>
      <li>Enter Text Here<span class="rule"></span></li>
      <li>Enter Text Here<span class="rule"></span></li>
    </ul>
  </section>

</body>
</html>
```